Metal Recycling Website Require New Design for upgrade

Our company currently have an existing website, www.tavorinmetal.com and the website is generally outdated so we would like an improvement.

We would generally prefer to keep the current color theme of our website as it is similar to our current logo.

We would also like our company factory picture to be on somewhere of the webpage (but only if the designer think that the picture can blend well with the color theme)

Our company is dealing alot Aluminiun, Stainless Steel, Copper, Brass, Iron

Pictures uploaded.

Target Market(s)

General Commercial Manufacturer, B2B

Industry/Entity Type

Recycling

Number of Pages Required

1 page

Colors

Designer to choose colors to be used in the design.

Requirements
Must have
• Hopefully color will be similar to my logo theme but designer welcome to have their own input.
Nice to have
• Company Picture (Uploaded in the file)

```html
<!DOCTYPE html>
<html lang="en">
<head>
<meta charset="utf-8">
<title>Tavorin Metal Recycling</title>
<link href="https://fonts.googleapis.com/css2?family=Poppins:wght@400;500&family=Saira:wght@500;600;700&display=swap" rel="stylesheet">
<style>
:root{
  --gold:#c9992f;
  --gold-soft:#d0a847;
  --ink:#4d4d4d;
  --heading-grey:#5e5e5e;
  --text:#3f3f3f;
  --light:#f4f4f4;
  --footer:#8d8d8d;
  --white:#ffffff;
  --line:#bdbdbd;
}
*{box-sizing:border-box;margin:0;padding:0}
html,body{width:1200px;height:3414px;overflow:hidden}
body{position:relative;background:var(--white);font-family:"Poppins",sans-serif;color:var(--text)}
section,header,footer{position:absolute;left:0;width:1200px}
.abs{position:absolute}
.heading{font-family:"Saira",sans-serif;font-weight:600;text-transform:uppercase;text-align:center;font-size:36px;letter-spacing:.3px;color:var(--heading-grey)}
.heading .accent{color:var(--gold)}
.btn{position:absolute;background:var(--gold);color:var(--white);font-family:"Saira",sans-serif;font-weight:600;display:flex;align-items:center;justify-content:center}

/* header */
.site-header{top:0;height:120px;background:var(--white)}
.brand{left:142px;top:27px;display:flex;align-items:center;gap:26px}
.brand-mark{width:76px;height:76px;border:3px solid var(--gold)}
.brand-name{font-family:"Saira",sans-serif;font-weight:600;font-size:30px;color:var(--gold);letter-spacing:1px;line-height:1}
.contact-bar{top:42px;left:700px;display:flex;gap:38px;font-size:14.5px;color:#333}
.contact-bar span{display:flex;align-items:center;gap:8px}
.nav{top:86px;left:609px;display:flex;gap:28px;font-family:"Saira",sans-serif;font-weight:500;font-size:15.5px;color:#777}
.nav .active{color:var(--gold)}

/* hero */
.hero{top:120px;height:565px;background:linear-gradient(135deg,#3a2a1e 0%,#5a3d28 25%,#2b2b2d 50%,#6b4a30 72%,#1f1f22 100%)}
.hero h1{position:absolute;left:120px;top:293px;width:960px;text-align:center;font-family:"Saira",sans-serif;font-weight:500;font-size:38px;line-height:43px;color:var(--white)}

/* about */
.about{top:685px;height:424px}
.about .heading{position:absolute;top:60px;width:100%}
.about .copy{position:absolute;left:150px;width:900px;top:145px;text-align:center;font-size:13.3px;line-height:23px}
.about .copy p{margin-bottom:8px}
.about .btn{left:526px;top:316px;width:147px;height:41px;font-size:16.5px}

/* products */
.products{top:1109px;height:725px}
.products-band{position:absolute;left:0;top:0;width:1200px;height:359px;background:linear-gradient(180deg,#c9a147 0%,#c49637 100%)}
.products h2{position:absolute;top:98px;width:100%;text-align:center;font-family:"Saira",sans-serif;font-weight:700;font-size:40px;color:var(--white)}
.products .lead{position:absolute;left:150px;width:900px;top:152px;text-align:center;color:var(--white);font-size:14.5px;line-height:25px}
.products-panel{position:absolute;left:107px;top:249px;width:986px;height:420px;background:var(--white)}
.product-card{position:absolute;top:291px;width:212px;height:355px;background:var(--white);box-shadow:0 3px 8px rgba(0,0,0,.18);text-align:center}
.product-photo{height:162px}
.product-card h3{margin-top:18px;font-family:"Saira",sans-serif;font-weight:500;font-size:19px;color:#222}
.product-card p{margin:8px 14px 0;font-size:13px;line-height:19px}
.product-card .btn{left:62px;top:306px;width:88px;height:26px;font-size:12.5px}

/* accreditations */
.accreditations{top:1834px;height:381px;background:radial-gradient(ellipse at center,#fbfbfb 0%,#e6e6e6 100%)}
.accreditations .heading{position:absolute;top:73px;width:100%}
.badge{position:absolute}

/* services */
.services{top:2215px;height:520px}
.services .heading{position:absolute;top:78px;width:100%}
.service{position:absolute;top:180px;width:300px;text-align:center}
.service-icon{margin:0 auto;width:117px;height:117px;border-radius:50%;border:5px solid var(--gold);background:#f7f7f7;display:flex;align-items:center;justify-content:center;box-shadow:0 10px 8px -6px rgba(0,0,0,.15)}
.service h3{margin-top:28px;font-family:"Saira",sans-serif;font-weight:600;font-size:19.5px;color:#333}
.service p{margin-top:14px;font-size:13.3px;line-height:23px}

/* footer */
.site-footer{top:3090px;height:278px;background:var(--footer);color:var(--white)}
.footer-title{font-family:"Saira",sans-serif;font-weight:500;font-size:17px;position:absolute;top:93px}
.footer-links{position:absolute;top:132px;font-size:13px;line-height:30.5px}
.footer-contact{position:absolute;left:449px;top:134px;font-size:13px;line-height:30px}
.footer-contact div{display:flex;align-items:center;gap:12px}
.footer-brand{left:808px;top:97px;width:250px;text-align:center}
.footer-brand .mark{width:68px;height:68px;margin:0 auto 16px;border:3px solid var(--gold);background:var(--white)}
.footer-brand .name{font-family:"Saira",sans-serif;font-weight:600;font-size:24px;letter-spacing:1px;line-height:1}
.copyright{left:0;top:3368px;width:1200px;height:46px;background:var(--gold);color:var(--white);font-size:12.5px;display:flex;align-items:center;justify-content:center;text-align:center}

/* inquiry */
.inquiry{left:229px;top:2742px;width:707px;height:371px;background:var(--white);border-radius:6px;box-shadow:0 4px 14px rgba(0,0,0,.18);z-index:2}
.stripe{position:absolute;left:57px;width:592px;height:5px;background:repeating-linear-gradient(90deg,var(--gold) 0 14px,#9a9a9a 14px 28px)}
.inquiry h2{position:absolute;top:26px;width:100%;text-align:center;font-family:"Saira",sans-serif;font-weight:600;font-size:32px;color:var(--heading-grey)}
.inquiry h2 .accent{color:var(--gold)}
.field{position:absolute;height:42px;border:1px solid #cfcfcf;border-radius:3px;display:flex;align-items:center;font-size:11px;color:#555}
.field .ic{width:36px;height:100%;border-right:1px solid #dcdcdc;display:flex;align-items:center;justify-content:center;margin-right:12px}
.field.message{align-items:flex-start;height:84px}
.field.message .ic{height:30px}
.field.message .label{padding-top:9px}
.inquiry .btn{left:264px;top:288px;width:147px;height:42px;font-size:16px}
</style>
</head>
<body>

<header class="site-header">
  <div class="brand abs">
    <div class="brand-mark"></div>
    <div class="brand-name">TAVORIN METAL</div>
  </div>
  <div class="contact-bar abs">
    <span><svg width="18" height="18" viewBox="0 0 24 24" fill="none" stroke="#c9992f" stroke-width="2"><path d="M5 3h4l2 5-3 2a11 11 0 0 0 6 6l2-3 5 2v4a2 2 0 0 1-2 2A17 17 0 0 1 3 5a2 2 0 0 1 2-2z"/></svg>+65-9000 4127</span>
    <span><svg width="20" height="18" viewBox="0 0 24 20" fill="none" stroke="#c9992f" stroke-width="2"><rect x="2" y="3" width="20" height="14"/><path d="M2 3l10 8 10-8"/></svg>sales@tavorinmetal.com</span>
  </div>
  <nav class="nav abs">
    <span class="active">Home</span><span>About Us</span><span>Products</span><span>Our Services</span><span>Contact Us</span>
  </nav>
</header>

<section class="hero">
  <div class="abs" style="inset:0" role="img" aria-label="Collage of scrap metal: steel beams, copper wire, crushed cans and engine parts"></div>
  <h1>We Have Become A Recycling Industry Leader In The Local Market, Committed To Responsibly And Efficiently</h1>
</section>

<section class="about">
  <h2 class="heading"><span class="accent">About Tavorin Metal</span> Recycling</h2>
  <div class="copy">
    <p>Tavorin Metal Recycling primary activities are the procurement, processing, recycling and trading of all ferrous and non-ferrous scrap metals, industrial scraps and other recyclables.</p>
    <p>We provide full-service ferrous and non-ferrous metal recycler and processor. Recognized as an industry leader in metal recycling, our team of experienced staff and trader understand the intricacies of scrap metal recycling.</p>
    <p>We build long term relationships with all our customer by understanding their needs and recommending customized solutions that are designed to improve efficiency and value of their scrap.</p>
  </div>
  <div class="btn">Read More</div>
</section>

<section class="products">
  <div class="products-band" role="img" aria-label="Company factory building with a gold tint"></div>
  <h2>Our Products</h2>
  <p class="lead">Lorem ipsum dolor sit amet, consectetuer adipiscing elit, sed diam nonummy nibh euismod tincidunt ut laoreet dolore magna aliquam erat volutpat. Ut wisi enim ad minim veniam, quis nostrud exerci tation ullamcorper suscipit.</p>
  <div class="products-panel"></div>

  <article class="product-card" style="left:140px">
    <div class="product-photo" role="img" aria-label="Bales of crushed aluminium" style="background:linear-gradient(135deg,#8f98a6,#cfd4dc 50%,#5b6370)"></div>
    <h3>Aluminium</h3>
    <p>Lorem ipsum dolor sit amet, consectetuer adipiscing elit, sed diam nonummy nibh euismod tincidunt.</p>
    <div class="btn">Read More</div>
  </article>
  <article class="product-card" style="left:375px">
    <div class="product-photo" role="img" aria-label="Stacked stainless steel scrap" style="background:linear-gradient(135deg,#6f7378,#c5c8cc 50%,#4a4d52)"></div>
    <h3>Stainless Steel</h3>
    <p>Lorem ipsum dolor sit amet, consectetuer adipiscing elit, sed diam nonummy nibh euismod tincidunt.</p>
    <div class="btn">Read More</div>
  </article>
  <article class="product-card" style="left:610px">
    <div class="product-photo" role="img" aria-label="Coiled copper wire" style="background:linear-gradient(135deg,#7a3a1e,#c9744a 50%,#8c4526)"></div>
    <h3>Copper</h3>
    <p>Lorem ipsum dolor sit amet, consectetuer adipiscing elit, sed diam nonummy nibh euismod tincidunt.</p>
    <div class="btn">Read More</div>
  </article>
  <article class="product-card" style="left:845px">
    <div class="product-photo" role="img" aria-label="Pile of brass fittings" style="background:linear-gradient(135deg,#6e5320,#d3a94a 50%,#8a6a2a)"></div>
    <h3>Brass</h3>
    <p>Lorem ipsum dolor sit amet, consectetuer adipiscing elit, sed diam nonummy nibh euismod tincidunt.</p>
    <div class="btn">Read More</div>
  </article>
</section>

<section class="accreditations">
  <h2 class="heading"><span class="accent">Our</span> Accreditations</h2>
  <div class="badge" style="left:163px;top:185px;width:255px;height:105px;background:#d9d9d9;border-radius:4px" role="img" aria-label="Workplace safety certification badge"></div>
  <div class="badge" style="left:483px;top:190px;width:155px;height:110px;background:#e4dcc5;border-radius:4px" role="img" aria-label="Business award badge"></div>
  <div class="badge" style="left:709px;top:190px;width:102px;height:102px;background:#cfe1ea;border-radius:50%" role="img" aria-label="Certification body badge"></div>
  <div class="badge" style="left:825px;top:190px;width:118px;height:102px;border:2px solid #2fa3d6;background:#f7f7f7" role="img" aria-label="Environmental management standard badge"></div>
  <div class="badge" style="left:952px;top:190px;width:80px;height:102px;background:#23468f" role="img" aria-label="Accreditation service badge"></div>
</section>

<section class="services">
  <h2 class="heading"><span class="accent">Our</span> Services For</h2>
  <div class="service" style="left:135px">
    <div class="service-icon"><svg width="48" height="48" viewBox="0 0 48 48" fill="#5a5a5a"><circle cx="24" cy="15" r="9"/><path d="M6 44c0-10 8-16 18-16s18 6 18 16z"/></svg></div>
    <h3>FOR INDIVIDUAL</h3>
    <p>Do Your Part, Recycle With Us Today, consectetuer adipiscing elit, sed diam nonummy nibh euismod.</p>
  </div>
  <div class="service" style="left:450px">
    <div class="service-icon"><svg width="50" height="46" viewBox="0 0 50 46" fill="none" stroke="#5a5a5a" stroke-width="3"><rect x="4" y="12" width="42" height="30" rx="3"/><path d="M18 12V6h14v6M4 24h42"/></svg></div>
    <h3>FOR CORPORATE</h3>
    <p>Get The Best Value For Your Scrap consectetuer adipiscing elit, sed diam nonummy nibh euismod.</p>
  </div>
  <div class="service" style="left:765px">
    <div class="service-icon"><svg width="50" height="50" viewBox="0 0 50 50" fill="none" stroke="#5a5a5a" stroke-width="2.5"><circle cx="25" cy="25" r="12"/><path d="M13 25h24M25 13v24M25 13c-6 6-6 18 0 24M25 13c6 6 6 18 0 24"/></svg></div>
    <h3>FOR INTERNATIONAL</h3>
    <p>Your Trusted Global Partner consectetuer adipiscing elit, sed diam nonummy nibh euismod.</p>
  </div>
</section>

<div class="inquiry abs">
  <div class="stripe" style="top:-4px"></div>
  <h2><span class="accent">Quick</span> Inquiry</h2>
  <div class="field" style="left:57px;top:87px;width:289px"><span class="ic">&#9679;</span>First Name*</div>
  <div class="field" style="left:360px;top:87px;width:291px"><span class="ic">&#9679;</span>Last Name*</div>
  <div class="field" style="left:57px;top:141px;width:289px"><span class="ic">&#9742;</span>Your Phone*</div>
  <div class="field" style="left:360px;top:141px;width:291px"><span class="ic">&#9993;</span>Your Email*</div>
  <div class="field message" style="left:57px;top:197px;width:594px"><span class="ic">&#9998;</span><span class="label">Your Message*</span></div>
  <div class="btn">SUBMIT</div>
  <div class="stripe" style="top:365px"></div>
</div>

<footer class="site-footer">
  <div class="footer-title" style="left:146px">Quick Links</div>
  <div class="footer-links" style="left:146px">&rsaquo;&nbsp; Home<br>&rsaquo;&nbsp; About Us<br>&rsaquo;&nbsp; Contact Us</div>
  <div class="footer-links" style="left:273px">&rsaquo;&nbsp; Products<br>&rsaquo;&nbsp; Our Services<br>&rsaquo;&nbsp; Terms of Use</div>
  <div class="footer-title" style="left:449px">Contact Details</div>
  <div class="footer-contact">
    <div><svg width="14" height="16" viewBox="0 0 14 18" fill="#fff"><path d="M7 0a7 7 0 0 1 7 7c0 5-7 11-7 11S0 12 0 7a7 7 0 0 1 7-7z"/><circle cx="7" cy="7" r="2.5" fill="#8d8d8d"/></svg>18 Harbourline Road, Singapore 600118</div>
    <div><svg width="14" height="16" viewBox="0 0 24 24" fill="none" stroke="#fff" stroke-width="2"><path d="M5 3h4l2 5-3 2a11 11 0 0 0 6 6l2-3 5 2v4a2 2 0 0 1-2 2A17 17 0 0 1 3 5a2 2 0 0 1 2-2z"/></svg>+65-9000 4127</div>
    <div><svg width="16" height="14" viewBox="0 0 24 20" fill="none" stroke="#fff" stroke-width="2"><rect x="2" y="3" width="20" height="14"/><path d="M2 3l10 8 10-8"/></svg>sales@tavorinmetal.com</div>
  </div>
  <div class="footer-brand abs">
    <div class="mark"></div>
    <div class="name">TAVORIN METAL</div>
  </div>
</footer>
<div class="copyright abs">Copyright © 2019 &nbsp; Tavorin Metal Recycling All Right Reserved.</div>

</body>
</html>
```